QB-Electronics advertising flag and billboard design

I need a design for advertising flag and a design for billboard.
Information can be obtained from https://qb-elektronik-example.de.
Target Market(s)
IT service for companies
Requirements
Must have
- Logo, contact information and services

```html
<!DOCTYPE html>
<html lang="de">
<head>
<meta charset="utf-8">
<title>QB-Elektronik – Billboard &amp; Werbefahne</title>
<link href="https://fonts.googleapis.com/css2?family=Archivo:wght@700;800;900&family=Roboto:wght@400;500&display=swap" rel="stylesheet">
<style>
  :root{
    --bg:#ffffff;
    --panel:#0d1014;
    --ink:#ffffff;
    --accent:#4a6fe3;
    --accent-deep:#2f4fd0;
    --glow:#5fd4ff;
    --muted:#dfe4ea;
  }
  *{box-sizing:border-box;margin:0;padding:0}
  html,body{width:1200px;height:1200px;overflow:hidden;background:var(--bg)}
  body{position:relative;font-family:"Roboto",Arial,sans-serif;color:var(--ink)}

  /* Billboard */
  .billboard{position:absolute;left:40px;top:330px;width:840px;height:430px;background:var(--panel);overflow:hidden}
  .billboard__visual{position:absolute;right:0;top:0;width:430px;height:100%;
    background:radial-gradient(circle at 48% 42%,rgba(95,212,255,.75) 0,rgba(40,120,190,.45) 18%,rgba(13,16,20,0) 48%),
               radial-gradient(circle at 60% 85%,rgba(120,90,80,.55) 0,rgba(13,16,20,0) 45%),
               linear-gradient(90deg,var(--panel) 0,#121b26 40%,#0f1822 100%)}
  .brand{position:absolute;left:48px;top:46px;font-family:"Archivo",Arial,sans-serif;font-weight:700;font-size:26px;letter-spacing:3px;text-transform:uppercase;color:var(--ink)}
  .headline{position:absolute;left:46px;top:96px;font-family:"Archivo",Arial,sans-serif;font-weight:900;font-size:60px;line-height:1.02;color:var(--ink)}
  .headline .accent{color:var(--accent)}
  .services{position:absolute;top:250px;list-style:none;font-size:17px;line-height:1.2}
  .services--left{left:48px}
  .services--right{left:300px;top:270px}
  .services li{display:flex;align-items:flex-start;gap:12px;margin-bottom:12px}
  .tick{flex:none;width:18px;height:18px}
  .contact{position:absolute;left:46px;top:362px;display:flex;align-items:center;gap:16px}
  .contact__icon{width:34px;height:34px}
  .contact__number{font-family:"Archivo",Arial,sans-serif;font-weight:900;font-size:44px;letter-spacing:1px}
  .web{position:absolute;right:50px;bottom:26px;border:2px solid var(--accent);padding:6px 14px;font-size:16px;letter-spacing:.5px;background:rgba(13,16,20,.6)}

  /* Flag */
  .flag{position:absolute;left:930px;top:120px;width:230px;height:960px;background:var(--panel);border-top-right-radius:230px 300px;border-top-left-radius:40px 80px;overflow:hidden}
  .flag__visual{position:absolute;left:0;top:0;width:100%;height:330px;
    background:radial-gradient(circle at 55% 35%,rgba(95,212,255,.75) 0,rgba(40,120,190,.4) 22%,rgba(13,16,20,0) 55%),
               linear-gradient(180deg,#15324a 0,#101a24 70%,var(--panel) 100%)}
  .flag__text{position:absolute;left:18px;top:360px;height:460px;writing-mode:vertical-rl;transform:rotate(180deg);display:flex;flex-direction:column;justify-content:flex-start}
  .flag__brand{font-family:"Archivo",Arial,sans-serif;font-weight:700;font-size:24px;letter-spacing:3px;text-transform:uppercase;margin-left:12px}
  .flag__headline{font-family:"Archivo",Arial,sans-serif;font-weight:900;font-size:52px;line-height:1.05}
  .flag__headline .accent{color:var(--accent)}
  .flag__band{position:absolute;left:0;bottom:0;width:100%;height:120px;background:linear-gradient(180deg,var(--accent-deep),var(--accent));display:flex;align-items:flex-start;justify-content:center;padding-top:22px;gap:8px}
  .flag__phone{font-family:"Archivo",Arial,sans-serif;font-weight:800;font-size:21px;color:var(--muted)}
  .flag__icon{width:20px;height:20px;margin-top:3px}
</style>
</head>
<body>

<section class="billboard">
  <div class="billboard__visual" role="img" aria-label="Hände halten ein Smartphone, darüber ein leuchtendes digitales Schutzschild mit Schloss"></div>
  <div class="brand">QB-Elektronik</div>
  <h1 class="headline">Ihr Partner<br><span class="accent">für</span> IT-Service</h1>

  <ul class="services services--left">
    <li><svg class="tick" viewBox="0 0 18 18"><circle cx="9" cy="9" r="9" fill="#2a2f36"/><path d="M5 9.5l3 3 5-6" stroke="#fff" stroke-width="2" fill="none"/></svg>Laptop Reparatur</li>
    <li><svg class="tick" viewBox="0 0 18 18"><circle cx="9" cy="9" r="9" fill="#2a2f36"/><path d="M5 9.5l3 3 5-6" stroke="#fff" stroke-width="2" fill="none"/></svg>Mac Reparatur</li>
    <li><svg class="tick" viewBox="0 0 18 18"><circle cx="9" cy="9" r="9" fill="#2a2f36"/><path d="M5 9.5l3 3 5-6" stroke="#fff" stroke-width="2" fill="none"/></svg>Data Backup and<br>Recovery</li>
  </ul>
  <ul class="services services--right">
    <li><svg class="tick" viewBox="0 0 18 18"><circle cx="9" cy="9" r="9" fill="#2a2f36"/><path d="M5 9.5l3 3 5-6" stroke="#fff" stroke-width="2" fill="none"/></svg>PC Reparatur</li>
    <li><svg class="tick" viewBox="0 0 18 18"><circle cx="9" cy="9" r="9" fill="#2a2f36"/><path d="M5 9.5l3 3 5-6" stroke="#fff" stroke-width="2" fill="none"/></svg>Malware and Virus Entfernen</li>
    <li><svg class="tick" viewBox="0 0 18 18"><circle cx="9" cy="9" r="9" fill="#2a2f36"/><path d="M5 9.5l3 3 5-6" stroke="#fff" stroke-width="2" fill="none"/></svg>Software Installation</li>
  </ul>

  <div class="contact">
    <svg class="contact__icon" viewBox="0 0 34 34"><circle cx="17" cy="17" r="17" fill="var(--accent)"/><path d="M12 9l3 0 1.5 4-2 1.5a10 10 0 0 0 5 5l1.5-2 4 1.5 0 3a2 2 0 0 1-2 2A14 14 0 0 1 10 11a2 2 0 0 1 2-2z" fill="#0d1014"/></svg>
    <span class="contact__number">01234-5550199</span>
  </div>
  <div class="web">qb-elektronik-example.de</div>
</section>

<section class="flag">
  <div class="flag__visual" role="img" aria-label="Leuchtendes digitales Schutzschild mit Schloss über einem Smartphone in Händen"></div>
  <div class="flag__text">
    <div class="flag__brand">QB-Elektronik</div>
    <div class="flag__headline">Ihr Partner<br><span class="accent">für</span> IT-Service</div>
  </div>
  <div class="flag__band">
    <svg class="flag__icon" viewBox="0 0 34 34"><circle cx="17" cy="17" r="17" fill="#0d1014"/><path d="M12 9l3 0 1.5 4-2 1.5a10 10 0 0 0 5 5l1.5-2 4 1.5 0 3a2 2 0 0 1-2 2A14 14 0 0 1 10 11a2 2 0 0 1 2-2z" fill="#dfe4ea"/></svg>
    <span class="flag__phone">01234-5550199</span>
  </div>
</section>

</body>
</html>
```